Velvet Lantern Takeaway

we are emergent restaurant, serving high end of vietnamese cuisine.

Takeaway flyer's purpose must catch people attention by visual and clear dishes's description.

Please use attached logo.
And some other design for inspiration.
Updates

FLYER SIZE: DL FOLDED A4- DOUBLED SIZE. I WILL PRINT IT IN FULL COLOR AND 150GSM STOCK PAPER GLOSSTHANKS ALLHOPE I WILL GET A GREAT ONE FROM YOUKAIREN Added Tuesday, February 17, 2015

Please use images of "Vietnamese Beef Noodle PHO" if you intent to use images in the flyer Added Wednesday, February 18, 2015

Industry/Entity Type

Restaurant

Requirements
Must have
• Restaurant logo
Nice to have
• Font is very important.

```html
<!DOCTYPE html>
<html lang="en">
<head>
<meta charset="utf-8">
<title>Velvet Lantern Takeaway – Menu</title>
<link href="https://fonts.googleapis.com/css2?family=Alfa+Slab+One&family=Arvo:ital,wght@0,400;0,700;1,700&family=Yellowtail&family=Righteous&display=swap" rel="stylesheet">
<style>
  :root {
    --bg: #ececec;
    --paper: #f4f4f4;
    --paper-mid: #fafafa;
    --orange: #e8845a;
    --teal: #1d8f9b;
    --teal-box: #178a94;
    --ink: #262626;
    --white: #ffffff;
  }
  * { box-sizing: border-box; margin: 0; padding: 0; }
  html, body { width: 1200px; height: 860px; overflow: hidden; background: var(--bg); }
  .flyer {
    position: absolute; left: 80px; top: 58px; width: 1030px; height: 720px;
    display: flex; background: var(--paper);
    box-shadow: 0 2px 6px rgba(0,0,0,0.25);
  }
  .panel { position: relative; width: 343.33px; height: 100%; text-align: center; padding-top: 42px; }
  .panel--middle { background: var(--paper-mid); }
  .section-title {
    font-family: "Alfa Slab One", serif; color: var(--orange);
    font-size: 16px; letter-spacing: 0.5px; margin-bottom: 12px; line-height: 20px;
  }
  .section-title .script {
    font-family: "Yellowtail", cursive; color: var(--ink);
    font-size: 19px; letter-spacing: 0;
  }
  .section { margin-bottom: 30px; }
  .dish { margin-bottom: 10px; line-height: 13px; }
  .dish-name {
    font-family: "Arvo", serif; font-weight: 700; color: var(--teal);
    font-size: 11px; text-transform: uppercase; letter-spacing: 0.2px;
  }
  .dish-desc { font-family: "Arvo", serif; color: var(--ink); font-size: 10.5px; padding: 0 30px; }
  .dish-desc em { font-weight: 700; }
  .menu-box {
    position: absolute; left: 24px; right: 14px; top: 568px; height: 130px;
    background: var(--teal-box); padding: 12px 18px; text-align: left;
  }
  .panel--middle .menu-box { left: 18px; right: 20px; }
  .menu-box .box-title {
    font-family: "Alfa Slab One", serif; color: var(--orange);
    font-size: 13px; letter-spacing: 0.4px; margin-bottom: 6px;
  }
  .menu-box p {
    font-family: "Arvo", serif; font-weight: 700; color: var(--white);
    font-size: 10.5px; line-height: 16.5px;
  }
  .menu-box p.note { font-style: italic; line-height: 14px; margin-bottom: 3px; }
  .order {
    position: absolute; left: 0; right: 0; top: 626px;
  }
  .order-phone { font-family: "Righteous", sans-serif; color: var(--teal); font-size: 24px; letter-spacing: 1.5px; }
  .order-note { font-family: "Arvo", serif; font-weight: 700; color: var(--orange); font-size: 11px; line-height: 15px; margin-top: 2px; }
</style>
</head>
<body>
<main class="flyer">
  <section class="panel panel--left">
    <div class="section">
      <h2 class="section-title">ENTRÉE</h2>
      <div class="dish"><div class="dish-name">Butter Fried Corn (GF) - 6.50</div><div class="dish-desc">Fried sweet corn &amp; dried shrimp in spring onion butter sauce</div></div>
      <div class="dish"><div class="dish-name">Summer Rolls (GF) (2Rolls) - 7.50</div><div class="dish-desc">Rice paper rolled with tiger prawns, pork, salads &amp; herbs</div></div>
      <div class="dish"><div class="dish-name">Home Made Spring Rolls (4pcs) - 7.50</div><div class="dish-desc">Pastry wrapped with chicken mince, taro, &amp; mushrooms</div></div>
      <div class="dish"><div class="dish-name">Prawn Pop (4pcs) - 8.50</div><div class="dish-desc">Fried marinated prawn paste on sugar cane sticks</div></div>
      <div class="dish"><div class="dish-name">Sugar Cane Beef (4pcs) - 7.50</div><div class="dish-desc">Fried lemongrass beef mince on sugar cane sticks</div></div>
      <div class="dish"><div class="dish-name">Traditional Vietnamese Fish Cakes - 8.50</div></div>
    </div>
    <div class="section" style="margin-top:42px">
      <h2 class="section-title"><span class="script">Refreshing</span> SALADS</h2>
      <div class="dish"><div class="dish-name">Warmed Beef Papaya Salad (GF) - 16.90</div><div class="dish-desc">Marinated Beef mixed with green papaya, pickles</div></div>
      <div class="dish"><div class="dish-name">Prawn Papaya Salad (GF) - 16.90</div><div class="dish-desc">Prawn salad with lotus pickles &amp; papaya</div></div>
      <div class="dish"><div class="dish-name">Green Apple Salad (GF) - 16.90</div><div class="dish-desc">Char-grilled beef slices with green apple salad</div></div>
      <div class="dish"><div class="dish-name">Squid Salad (GF) - 16.90</div><div class="dish-desc">Steamed squid with pickles &amp; cucumber</div></div>
      <div class="dish"><div class="dish-name">Chicken Salad (GF) - 16.90</div><div class="dish-desc">Steamed chicken with plain cabbages &amp; pickles</div></div>
    </div>
    <div class="menu-box">
      <h3 class="box-title">VERMICELLI NOODLES SALAD</h3>
      <p>Stir-Fry Lemongrass Beef with Noodles - 13.90</p>
      <p>Sugar Cane Beef with Noodles - 13.90</p>
      <p>Sugar Cane Prawn Cake with Noodles - 13.90</p>
      <p>Chicken Spring Roll with Noodles - 13.90</p>
      <p>Char-grilled Pork Skewer with Noodles - 13.90</p>
    </div>
  </section>

  <section class="panel panel--middle">
    <div class="section">
      <h2 class="section-title">WE LOVE PHO</h2>
      <div class="dish"><div class="dish-name">Flat Rice Noodles Soup</div><div class="dish-desc"><em>with Your Choice of:</em></div></div>
      <div class="dish" style="margin-top:14px"><div class="dish-name">Beef - Small 9.50 <span style="color:var(--ink)">/</span> Regular 14.50</div></div>
      <div class="dish" style="margin-top:14px"><div class="dish-name">Chicken - Small 9.50 <span style="color:var(--ink)">/</span> Regular 13.50</div></div>
      <div class="dish" style="margin-top:14px"><div class="dish-name">Tofu &amp; Vegetables - Small 9.50 <span style="color:var(--ink)">/</span> Regular 13.50</div></div>
    </div>
    <div class="section" style="margin-top:36px">
      <h2 class="section-title">RICE <span class="script">is Nice</span></h2>
      <div class="dish"><div class="dish-name">Coconut Rice - 8.90</div></div>
      <div class="dish" style="margin-top:14px"><div class="dish-name">Seafood Fried Rice - 15.90</div><div class="dish-desc">Fried rice with prawns, squids, mussels &amp; mixed vegetables</div></div>
      <div class="dish"><div class="dish-name">Fried Rice - 12.90</div><div class="dish-desc">Fried rice with egg &amp; mixed vegetables</div></div>
      <div class="dish" style="margin-top:14px"><div class="dish-name">Steamed Rice - 3.00</div></div>
    </div>
    <div class="section" style="margin-top:36px">
      <h2 class="section-title">HOT SOUP <span class="script">- Dinner</span></h2>
      <div class="dish"><div class="dish-name">Scallop Soup - 8.50</div><div class="dish-desc">Thick soup with scallops, egg, corns cream &amp; carrot</div></div>
      <div class="dish"><div class="dish-name">Crabmeat &amp; Asparagus Soup - 8.50</div><div class="dish-desc">Delicious crabmeat soup with asparagus, egg &amp; carrot</div></div>
      <div class="dish"><div class="dish-name">Vietnamese Signature Hot Sour Soup - 8.50</div><div class="dish-desc">Barramundi in soup with beansprouts, tomato &amp; pineapple</div></div>
      <div class="dish"><div class="dish-name">Chicken Corns Soup - 8.50</div><div class="dish-desc">Thick Soup with eggs, carrots, corns cream</div></div>
    </div>
    <div class="menu-box">
      <h3 class="box-title">STIR-FRY NOODLES</h3>
      <p class="note">Your choice of: Lemongrass Beef, Chicken, Seafood, Tofu</p>
      <p>Stir-fry Egg Noodles - 13.90</p>
      <p>Stir-fry Flat Rice Noodles - 13.90</p>
      <p>Stir-fry Rice Vermicelli Noodles - 13.90</p>
    </div>
  </section>

  <section class="panel panel--right">
    <div class="section">
      <h2 class="section-title">VEGETARIAN <span class="script">Time</span></h2>
      <div class="dish"><div class="dish-name">Spring Rolls - 6.50</div><div class="dish-desc">Fried Pastry wrapped with crushed tofu, taro, mushrooms</div></div>
      <div class="dish"><div class="dish-name">Winter Rolls - 6.50</div><div class="dish-desc">Rice Paper Rolls with tofu, lettuces, vermicelli &amp; mints</div></div>
      <div class="dish"><div class="dish-name">Salt and Pepper Tofu - 11.50</div></div>
      <div class="dish" style="margin-top:11px"><div class="dish-name">Refreshing Beancurd Salad - 13.50</div></div>
      <div class="dish" style="margin-top:11px"><div class="dish-name">Stir-Fry Mushroom and Vegetables - 13.50</div></div>
      <div class="dish" style="margin-top:11px"><div class="dish-name">Pineapple and Beancurd Wok Tossed - 13.50</div></div>
      <div class="dish" style="margin-top:11px"><div class="dish-name">Claypot Tofu and Mushroom - 13.50</div><div class="dish-desc">Marinated Tofu and mushroom in coconut juice</div></div>
      <div class="dish"><div class="dish-name">Stir Fry Chilli Lemongrass Bean Curd<br>(Hot) - 13.50</div></div>
      <div class="dish" style="margin-top:11px"><div class="dish-name">Vermicelli Noodles Salad with Tofu - 13.50</div></div>
      <div class="dish" style="margin-top:11px"><div class="dish-name">Vegetarian Fried Rice - 13.50</div></div>
      <div class="dish" style="margin-top:11px"><div class="dish-name">Fried Noodles - 13.50</div></div>
    </div>
    <div class="section" style="margin-top:32px">
      <h2 class="section-title"><span class="script">We Mean</span> GREEN</h2>
      <div class="dish"><div class="dish-name">Green Wok Tossed - 12.90</div><div class="dish-desc">Asian mixed vegetables wok tossed</div></div>
      <div class="dish"><div class="dish-name">Baby Bok Choy with Mushroom - 12.90</div><div class="dish-desc"><em>Your Choice:</em><br>· Steam with Soy sauce OR Garlic sauce<br>· Stir-fry with Soy Sauce OR Garlic sauce</div></div>
      <div class="dish"><div class="dish-name">Steam Chinese Broccoli<br>with Oyster Sauce - 12.90</div></div>
      <div class="dish" style="margin-top:11px"><div class="dish-name">Water Spinach Tossed with Garlic Sauce<br>(Seasonal) - 12.90</div></div>
    </div>
    <div class="order">
      <div class="order-phone">0400 555 218</div>
      <div class="order-note">FREE HOME DELIVERY ORDERS<br>VIA TEXT MESSAGES</div>
    </div>
  </section>
</main>
</body>
</html>
```